Help me create an amazing cover for my first ebook!!

I am looking to have a modern and professional looking cover for my first ebook. It will be published through Borvex Quill Self Press and will need to follow their formatting and guidelines. I want the cover to have a modern and vibrant feel, that appeals to a millennial audience. This is a real estate book that is focused on a niche category catered to young professionals, so the idea would be to appeal to them.

Title:
The Twentysomething Playbook for Duplex Living

A Smart Property Buying Plan to Start Early, Cut Your Housing Costs (Sometimes to Zero), and Speed Up Your Path to Lasting Wealth.

Davin Osterlund

Target Market(s)

Real Estate investors, investors, millennials, young professionals, college educated, 20-40 years old.Financial freedom, finance.

Industry/Entity Type

Real Estate

Font styles to use
Sans Serif

Colors

Designer to choose colors to be used in the design.

Requirements
Must have
• Must follow the borvex quill self press format. I attached a screenshot of the details, it can also be found here: https://qsp.borvexbooks.example/en_US/help/topic/R481736025
• Must include this title:
• The Twentysomething Playbook for Duplex Living
• A Smart Property Buying Plan to Start Early, Cut Your Housing Costs (Sometimes to Zero), and Speed Up Your Path to Lasting Wealth.
• Davin Osterlund.
• I added examples of book covers I like to use as a guide, I also added some color pallette examples.
Nice to have
• Modern, clean design that's not too busy. Some sort of simple photo or illustration to incorporate in the cover along with the text would be nice.

```html
<!DOCTYPE html>
<html lang="en">
<head>
<meta charset="utf-8">
<title>The Twentysomething Playbook for Duplex Living — Davin Osterlund</title>
<link rel="stylesheet" href="https://fonts.googleapis.com/css2?family=Source+Code+Pro:wght@600;700;800&display=swap">
<style>
  :root {
    --paper: #ffffff;
    --ink: #2e3440;
    --ink-strong: #1c2029;
    --art-dark: #3b4656;
    --art-light: #eef1f5;
    --band: #4f6275;
    --band-text: #ffffff;
  }
  * { margin: 0; padding: 0; box-sizing: border-box; }
  html, body { width: 751px; height: 1200px; overflow: hidden; background: var(--paper); }
  .cover {
    position: relative;
    width: 751px;
    height: 1200px;
    background: var(--paper);
    font-family: "Source Code Pro", monospace;
    color: var(--ink);
  }
  .author {
    position: absolute;
    top: 100px;
    left: 0;
    width: 100%;
    text-align: center;
    font-size: 64px;
    font-weight: 700;
    line-height: 1;
  }
  .series-line {
    position: absolute;
    top: 202px;
    left: 0;
    width: 100%;
    text-align: center;
    font-size: 25px;
    font-weight: 700;
    color: var(--ink-strong);
    line-height: 1;
  }
  .cover-art {
    position: absolute;
    top: 290px;
    left: 36px;
    width: 678px;
    height: 356px;
    background: linear-gradient(180deg, var(--art-light) 0%, #c9d1db 55%, var(--art-dark) 100%);
  }
  .title {
    position: absolute;
    top: 700px;
    left: 0;
    width: 100%;
    text-align: center;
    font-weight: 700;
    font-size: 96px;
    line-height: 112px;
  }
  .title .word-one { display: block; letter-spacing: 0.42em; padding-left: 0.42em; }
  .title .word-two { display: block; letter-spacing: 0.12em; padding-left: 0.12em; }
  .title-rule {
    position: absolute;
    top: 951px;
    left: 159px;
    width: 429px;
    height: 19px;
    background: var(--ink);
  }
  .tagline-band {
    position: absolute;
    top: 998px;
    left: 0;
    width: 100%;
    height: 202px;
    background: var(--band);
    display: flex;
    align-items: center;
    justify-content: center;
    padding: 0 48px;
  }
  .tagline {
    color: var(--band-text);
    font-size: 23px;
    font-weight: 700;
    line-height: 32px;
    text-align: center;
  }
</style>
</head>
<body>
  <main class="cover">
    <p class="author">Davin Osterlund</p>
    <p class="series-line">The Twentysomething Playbook for</p>

    <div class="cover-art" role="img" aria-label="Cover illustration: a simple house roof with a four-pane window and a row of dollar signs"></div>

    <h1 class="title">
      <span class="word-one">Duplex</span>
      <span class="word-two">Living</span>
    </h1>
    <div class="title-rule"></div>

    <section class="tagline-band">
      <p class="tagline">A Smart Property Buying Plan to Start Early, Cut Your Housing Costs (Sometimes to Zero), and Speed Up Your Path to Lasting Wealth.</p>
    </section>
  </main>
</body>
</html>
```